New Website for Asia Travel Agency

Lanternpath Journeys Website

We want a redesign for our current website, www.lanternpathjourneys.example. We want you to get creative with our brand and present our company in a unique, creative and compelling way, that communicates our exotic destinations and tours, the local and authentic character of our travel consultants and the trustworthy and professional nature of our company.

Who is this company?

Lanternpath Journeys is an online tour operator specializing in providing tailor-made tours to eight destinations in Asia; Vietnam, Thailand, Laos, Cambodia, Indonesia, Myanmar, Japan and China. They were launched in mid February 2012 with headquarters in Bangkok, Thailand, and staffed by locals and expats with many years of experience in the travel industry, and who are committed to sharing their deep knowledge of, and passion for the region.

Local knowledge

Our consultants at Lanternpath Journeys are all locals – they know their destinations inside-out and draw upon invaluable first-hand experience and information when planning your tour. They have insights into local culture and tradition, they know the best places to visit, the most worthwhile experiences to have and, most importantly, they have the knowledge to create exactly the holiday you desire.

All hotels and activities featured in a Lanternpath Journeys tour are regularly inspected by our consultants to ensure the highest quality standards are met and that all information is correct and up to date.

Unforgettable Travel Experiences

Whether it's a cultural exploration or a beach holiday you're after – or a mix of both – Lanternpath Journeys has an itinerary for you – and if we don't have one, we'll tailor-make one! From the main sights to remote villages, our locally based Travel Specialists will give you unique insights into every place you visit and let you delve into known destinations from new perspectives.

Our tours offer a variety of hotel and resort options, premium stays in deluxe accommodation, heritage hotels, a five-star boutique or on the water in a junk. Tap into our experience let us create an experience unique to you – and one you will never forget.

What type of Holiday to Asia?

Our itineraries at Lanternpath Journeys are created according to different inspirations. Some travelers are interested in the History & Culture of a destination, while some like to stay active with Adventure tours. A Cross Border trip explores different countries in a single tour, while Velvet Summit tours offer the highest level of exclusivity across our destinations. There are 14 different Holiday Types to choose from, or you can mix and match ideas to create your dream vacation.

Target Market(s)

Slightly more female, aged 30-65, are creative, professional and looking for something different, something a bit unusual.

Industry/Entity Type

Boutique

Requirements
Must have
• 5 page designs:

1. Homepage
2. Tours list page for a country
3. Tour page
4. 'Be Inspired' page
5. Country page
6. Enquiry page

Our inspirations.

The following list shows websites we love and which inspire us... to give you some indication of our preferred styles, functions and layouts:

http://www.frostmeridian.example/en/ (we really like this, great personality, like the use of icons for tour types)
http://www.pebblewalks.example.uk/ (very simple design elements and layout)
http://www.sunvalecoast.example/ (great use of background image, nice simple nav bar)
http://www.roamcedarfall.example/ (we like because it has distinct personality and is well suited to the destination)
http://www.seemarlowton.example/ (clear personality through font use)
http://www.vastroving.example/ (original, unique)
http://www.wanderquill.example/long-loop-of-asia (like the map style)

Key design points:

1. You must use our existing logo (attached), but you can change the color scheme of the logo to accord with the whichever color scheme you choose for the main designs.
2. Our logo strapline is "Asia is our Lanternpath" and should be used prominently on the page to reinforce the meaning of our company name.
3. Home page and tours list pages should allow the user to see the choice of tours immediately without scrolling & Introduction copy should be minimal.
4. We and our site visitors are inspired and excited by our photography, this is an element of the site which we would like to maintain and build on, though the section page header sliders are currently too big and do not allow quick access to the section content. This is a design problem which needs a solution. Full page photographic backgrounds may be an answer?
5. Tour page should display other contextual tours, from the same country or style/type
6. We should promote press coverage in various places
7. We should display consultant profiles in various places
8. Map designs for tour page and country page, plus a modal pop out for the home page. These are complex and may have a few small photos and short descriptive text only, though this is limited by your own creativity. We will use graphics and html5/css3 so there are no creative limitations.
9. The 'Inspirations' / 'Be Inspired' page is for people who want travel and holiday ideas, who are looking for inspiration on where to go and what to do. This section needs to reflect the exotic, the unusual, the extraordinary in our destinations and tours, and we leave this to your creative genius to develop. We are also interested in how this inspirations page is related to the blog and social media content we produce daily, is there an integration here? Can we present YouTube videos, our blog posts, Friendwall posts etc, on this page? This is another design challenge.
10. We would like to see designs for the tours list page which feature AJAX content filtering (for instance: http://demo.layoutbrisk.example/?acn), we would like to see how to include this type of content filtering on homepage and destination page also.
11. The 'Enquiry' call to action should be on all pages and prominent.
12. The enquiry page can reflect the same fields as the existing website enquiry page

Values to be communicated:

- Exotic: Asia is exotic, and our tours will expose clients to extraordinary sights and unusual cultural encounters.
- Authentic: Our travel consultants all live in the destinations themselves, they are local nationals and have all the insider knowledge to give clients a truly authentic experience of our destinations
- Unique: All of our tours are tailor made, there are no fixed departure dates or join-in groups. All tour itineraries can be uniquely designed for our clients, from departure dates to destinations.
- Trust: Some travelers prefer to book their holidays with local agencies they can meet in person, rather than with online companies like us who live in the destinations and who they only get to meet on Skype video or phone. We want to convey that we are trustworthy. We have attempted this through presenting a 'meet the team' page and a 'press' page and advert, as well as offering a prominent international phone number. How we you build on this and further convey this value?

```html
<!DOCTYPE html>
<html lang="en">
<head>
<meta charset="utf-8">
<title>Lanternpath Journeys</title>
<link rel="stylesheet" href="https://fonts.googleapis.com/css2?family=Bebas+Neue&family=Open+Sans:wght@400;600;700&family=Rancho&family=Yanone+Kaffeesatz:wght@400;600&display=swap">
<style>
:root{
  --header-dark:#2f3d3d;
  --header-deep:#243030;
  --nav-light:#b9cfcc;
  --panel-dark:#2c3838;
  --brand-red:#c8101a;
  --link-blue:#1f5fa8;
  --ink:#222;
  --footer:#1b1b1b;
  --footer-text:#6e6e6e;
  --white:#fff;
}
*{margin:0;padding:0;box-sizing:border-box}
html,body{width:845px;height:1200px;overflow:hidden;background:var(--white)}
body{position:relative;font-family:"Open Sans",Arial,sans-serif;color:var(--ink)}
.abs{position:absolute}

.site-header{left:0;top:0;width:845px;height:154px;background:linear-gradient(#3a4a4a,var(--header-deep))}
.brand{left:30px;top:30px;display:flex;align-items:center;gap:10px}
.brand-mark{width:26px;height:26px;background:#cfe2df;border-radius:3px;flex:none}
.brand-name{font-size:20px;font-weight:600;color:var(--white);line-height:1;white-space:nowrap}
.brand-tag{font-size:10px;color:#d6dede;margin-top:3px;text-align:right;white-space:nowrap}
.account{left:626px;top:28px;font-size:10px;color:#e5eaea;line-height:20px}
.account .row{display:flex;align-items:center;gap:8px}
.account b{font-weight:700}
.search-field{left:649px;top:71px;width:148px;height:17px;background:var(--white);border:1px solid #ccc}
.search-icon{left:626px;top:73px}

.main-nav{left:29px;top:113px;width:785px;height:41px;background:var(--nav-light);border-radius:3px 3px 0 0;font-size:11px;color:#233}
.main-nav a{position:absolute;top:13px;transform:translateX(-50%);text-decoration:none;color:inherit;white-space:nowrap}
.main-nav .active{left:21px;transform:none;top:0;width:71px;height:41px;background:var(--header-deep);color:var(--white);display:flex;align-items:center;justify-content:center}

.hero{left:0;top:154px;width:845px;height:410px;background:linear-gradient(180deg,#5b8a4a 0%,#c9d6cf 35%,#e8eeea 55%,#7da86a 78%,#4f7a3a 100%)}
.hero-title{left:29px;top:154px;width:324px;height:77px;background:rgba(242,246,246,.92);border-radius:0 0 4px 4px;font-family:"Bebas Neue",sans-serif;font-weight:400;font-size:34px;color:#263232;display:flex;align-items:center;justify-content:center;letter-spacing:.5px;white-space:nowrap}
.quick-search{left:625px;top:154px}
.quick-title{left:658px;top:160px;font-family:"Rancho",cursive;font-size:27px;color:var(--white);white-space:nowrap}
.select{left:642px;width:155px;height:17px;background:var(--white);border:1px solid #ccc;font-size:9px;color:#888;padding-left:7px;line-height:15px}
.select::after{content:"";position:absolute;right:7px;top:6px;border:4px solid transparent;border-top:5px solid #222}
.qs-link{font-size:9.5px;color:var(--white);line-height:11px}
.dots{left:694px;top:530px;display:flex;gap:6px}
.dots span{width:10px;height:9px;background:#111}

.sub-nav{left:29px;top:564px;width:556px;height:40px;background:var(--panel-dark);border-radius:0 0 3px 3px;font-size:11px;color:#e8eeee}
.sub-nav a{position:absolute;top:14px;transform:translateX(-50%);color:inherit;text-decoration:none;white-space:nowrap}
.sub-nav .active{left:300px;top:0;width:71px;height:40px;transform:none;background:var(--nav-light);color:#233;display:flex;align-items:center;justify-content:center}
.emergency{left:600px;top:575px;width:240px;text-align:center;font-size:11px;line-height:16px}
.emergency .red{color:var(--brand-red);font-weight:700}
.emergency .blue{color:var(--link-blue)}

.promo{left:29px;top:640px;width:259px;height:270px;border-radius:3px;overflow:hidden;background:var(--brand-red)}
.promo-photo{width:259px;height:180px;background:linear-gradient(180deg,#6a5aa6 0%,#d86a86 45%,#e8925a 70%,#1b2235 100%)}
.promo-caption{left:0;top:180px;width:259px;height:90px;display:flex;align-items:center;justify-content:center;font-family:"Yanone Kaffeesatz",sans-serif;font-size:40px;font-weight:600;color:var(--white);white-space:nowrap}
.promo-caption span{color:#ffe000;margin-left:8px}
.ribbon{left:13px;top:0}
.ribbon-text{left:13px;top:4px;width:43px;text-align:center;font-family:"Bebas Neue",sans-serif;font-size:17px;line-height:15px;color:#ffe000}

.feature-title{left:328px;top:634px;width:257px;font-family:"Bebas Neue",sans-serif;font-weight:400;font-size:50px;color:var(--brand-red);line-height:50px;text-align:right;white-space:nowrap}
.feature-sub{left:328px;top:684px;width:257px;font-family:"Yanone Kaffeesatz",sans-serif;font-size:28px;color:#222;text-align:center;line-height:30px;white-space:nowrap}
.feature-points{left:328px;top:716px;width:257px;display:flex;justify-content:space-between;font-family:"Yanone Kaffeesatz",sans-serif;font-size:17px;line-height:20px;color:var(--brand-red);white-space:nowrap}
.feature-points span::before{content:"•";margin-right:7px}
.feature-rule{left:328px;top:742px;width:257px;height:1px;background:#ccc}
.story-head{left:328px;top:752px;display:flex;align-items:center;gap:8px;font-size:13px;line-height:18px;white-space:nowrap}
.share-dot{width:14px;height:14px;background:#3b5a98}
.story-text{left:328px;top:776px;width:257px;font-family:Arial,Helvetica,sans-serif;font-size:9.2px;line-height:11.5px;text-align:justify;color:#333}
.go-btn{left:519px;top:849px;width:66px;height:26px;background:var(--brand-red);color:var(--white);font-size:10px;display:flex;align-items:center;justify-content:center}
.rule{left:328px;top:875px;width:191px;height:1px;background:#bbb}
.pager{left:328px;top:893px;width:257px;height:17px;font-size:9.5px}
.pager .step{position:absolute;top:0;width:18px;height:17px;background:#e3e3e3;text-align:center;line-height:16px}
.pager .pages{position:absolute;left:78px;top:2px;width:100px;text-align:center;letter-spacing:1px;white-space:nowrap}

.newsletter{left:625px;top:638px;width:191px;height:272px;background:var(--panel-dark);border-radius:4px}
.news-brand{left:10px;top:9px;width:171px;height:50px;background:#3c4a4a;border-radius:2px;display:flex;align-items:center;gap:7px;padding-left:9px}
.news-brand .brand-mark{width:18px;height:18px}
.news-brand .brand-name{font-size:11px}
.news-brand .brand-tag{font-size:6.5px}
.news-copy{left:17px;top:69px;width:165px;font-size:10.5px;line-height:12px;color:#e4eaea}
.news-field{left:17px;width:155px;height:17px;background:var(--white);font-size:9px;color:#777;padding-left:8px;line-height:17px}
.news-more{left:26px;top:222px;font-size:10px;color:var(--white);white-space:nowrap}
.subscribe{left:107px;top:219px;width:65px;height:19px;background:var(--brand-red);color:var(--white);font-size:10px;display:flex;align-items:center;justify-content:center}

.strip{left:29px;top:944px;width:787px;height:41px;background:#e7e7e7;border-radius:3px}

.site-footer{left:0;top:1019px;width:845px;height:181px;background:var(--footer)}
.foot-col{top:38px;font-size:11px;line-height:20px;color:var(--footer-text);white-space:nowrap}
.foot-col h4{font-weight:600;font-size:11px;color:#7a7a7a}
.foot-divider{top:0;width:1px;height:120px;background:#262626}
</style>
</head>
<body>

<header class="abs site-header">
  <div class="abs brand">
    <div class="brand-mark"></div>
    <div>
      <div class="brand-name">Lanternpath Journeys</div>
      <div class="brand-tag">Asia is our Lanternpath</div>
    </div>
  </div>
  <div class="abs account">
    <div class="row">
      <svg width="11" height="11" viewBox="0 0 12 12"><circle cx="6" cy="3.5" r="3" fill="#cdd6d6"/><path d="M0 12c0-4 3-5 6-5s6 1 6 5z" fill="#cdd6d6"/></svg>
      <span>Welcome ( log in ) | Sign Up</span>
    </div>
    <div class="row" style="font-size:11px">
      <svg width="11" height="11" viewBox="0 0 12 12"><path d="M1 8V6a5 5 0 0 1 10 0v2" stroke="#cdd6d6" stroke-width="1.6" fill="none"/><rect x="0" y="7" width="3" height="4" fill="#cdd6d6"/><rect x="9" y="7" width="3" height="4" fill="#cdd6d6"/></svg>
      <span>Happy to help <b>88888 88888</b></span>
    </div>
  </div>
  <svg class="abs search-icon" width="13" height="13" viewBox="0 0 13 13"><circle cx="5" cy="5" r="3.8" stroke="#dde" stroke-width="1.8" fill="none"/><path d="M8 8l4 4" stroke="#dde" stroke-width="2"/></svg>
  <div class="abs search-field"></div>
</header>

<nav class="abs main-nav">
  <a class="active" href="#">HOME</a>
  <a href="#" style="left:148px">DESTINATION</a>
  <a href="#" style="left:246px">PACKAGE</a>
  <a href="#" style="left:349px">SPECIAL TOURS</a>
  <a href="#" style="left:444px">DEALS</a>
  <a href="#" style="left:545px">ONLINE BOOKING</a>
  <a href="#" style="left:653px">CONTACT</a>
  <a href="#" style="left:729px">BLOG</a>
</nav>

<div class="abs hero" role="img" aria-label="Photograph of tall jungle waterfalls cascading into a river among green hills"></div>
<h1 class="abs hero-title">ASIA IS OUR LANTERNPATH</h1>

<svg class="abs quick-search" width="189" height="270" viewBox="0 0 189 270">
  <polygon points="0,0 189,0 189,270 95,190 0,270" fill="rgba(255,255,255,.28)"/>
</svg>
<div class="abs quick-title">Quick Search</div>
<div class="abs select" style="top:204px">Asia</div>
<div class="abs select" style="top:238px">July 14</div>
<div class="abs select" style="top:272px">Lorem Ipsum</div>
<div class="abs select" style="top:305px">Lorem Ipsum</div>
<svg class="abs" style="left:714px;top:332px" width="14" height="14" viewBox="0 0 13 13"><circle cx="5" cy="5" r="3.8" stroke="#fff" stroke-width="1.8" fill="none"/><path d="M8 8l4 4" stroke="#fff" stroke-width="2"/></svg>
<div class="abs qs-link" style="left:641px;top:355px">Advanced<br>Search</div>
<div class="abs qs-link" style="left:759px;top:355px;text-align:right">Greatest<br>Deals</div>
<div class="abs dots"><span></span><span></span><span></span><span></span></div>

<nav class="abs sub-nav">
  <a href="#" style="left:102px">FIRST TIME CRUISER ?</a>
  <a href="#" style="left:236px">BOOK WITH US</a>
  <a class="active" href="#">DEALS</a>
  <a href="#" style="left:417px">PACKAGES</a>
  <a href="#" style="left:497px">NEWS</a>
</nav>
<div class="abs emergency">
  <div class="red">24 HOUR EMERGENCY</div>
  <div class="blue">TRAVEL PROTECTION GUARANTEED</div>
</div>

<section class="abs promo">
  <div class="promo-photo" role="img" aria-label="Photograph of a Bangkok temple spire at sunset"></div>
  <svg class="abs ribbon" width="43" height="62" viewBox="0 0 43 62"><polygon points="0,0 43,0 43,62 21.5,50 0,62" fill="var(--brand-red)"/></svg>
  <div class="abs ribbon-text">20%<br>OFF</div>
  <div class="abs promo-caption">amezing<span>Bangkok</span></div>
</section>

<h2 class="abs feature-title">WORLD IS MINE</h2>
<div class="abs feature-sub">Go anywhere in world</div>
<div class="abs feature-points"><span>Special Deal</span><span>Book Online</span><span>Fast Process</span></div>
<div class="abs feature-rule"></div>
<div class="abs story-head">Amezing Bangkok <span class="share-dot"></span></div>
<p class="abs story-text">ellentesque sollicitudin ante magna, eget egestas ligula semper eget. Donec ac malesuada tortor. Suspendisse in varius elit. Donec er molestie orci volutpat congue congue. Proin lectus elit, volutpat vitae lobortis ut, feugiat nec velit. Proin id laoreet massa. at congue congue. Proin lectus elit volutpat</p>
<div class="abs go-btn">Go for it</div>
<div class="abs rule"></div>
<div class="abs pager">
  <div class="step" style="left:0">-</div>
  <div class="pages">1 | <b>2</b> | 3 | 4 | 5</div>
  <div class="step" style="right:0">+</div>
</div>

<aside class="abs newsletter">
  <div class="abs news-brand">
    <div class="brand-mark"></div>
    <div>
      <div class="brand-name">Lanternpath Journeys</div>
      <div class="brand-tag">Asia is our Lanternpath</div>
    </div>
  </div>
  <p class="abs news-copy">Sign up for our newsletter and receive our best deals in your inbox.</p>
  <div class="abs news-field" style="top:117px">Name</div>
  <div class="abs news-field" style="top:151px">Email</div>
  <div class="abs news-field" style="top:185px">Contact Number</div>
  <div class="abs news-more">More about it</div>
  <div class="abs subscribe">Subscribe</div>
</aside>

<div class="abs strip"></div>

<footer class="abs site-footer">
  <div class="abs foot-divider" style="left:179px"></div>
  <div class="abs foot-divider" style="left:339px"></div>
  <div class="abs foot-divider" style="left:500px"></div>
  <div class="abs foot-divider" style="left:660px"></div>
  <div class="abs foot-col" style="left:66px"><h4>Useful links</h4>dolor sit amet<br>sit ut duis<br>molestie<br>augue homero</div>
  <div class="abs foot-col" style="left:226px"><h4>Onlie Info</h4>dolor sit amet<br>sit ut duis<br>molestie<br>augue homero</div>
  <div class="abs foot-col" style="left:376px"><h4>About us</h4>dolor sit amet<br>sit ut duis<br>molestie<br>augue homero</div>
  <div class="abs foot-col" style="left:548px"><h4>Deals</h4>dolor sit amet<br>sit ut duis<br>molestie<br>augue homero</div>
  <div class="abs foot-col" style="left:710px"><h4>Follow us on</h4>Friendwall<br>Chirpline<br>Linkcircle<br>Searchly Plus</div>
</footer>

</body>
</html>
```